Onboarding Infographic/brochure

We are a small criminal defense firm looking to create some sort of infographic or brochure that we can onboard new clients with. We are currently sending it out via email but want something a bit cooler and fun to send to clients. The information is:

A Few Quick Rules

We are here to help each step of the way. While questions are never discouraged, this letter will answer some of the most common ones we get asked.

Communications

As a client, you should always be in the loop. While we will try to respond to questions as quickly as possible, sometimes we are unable to respond right away. Do not worry - we promise to get back to you soon. Some questions might take some time to research, and a correct answer is better than a quick one.

Appointments

One of the benefits of having an attorney is the ability to discuss your case outside of court, minus the stress and headaches. If you need an appointment, please contact the office.

Appointments must be scheduled in advance. We do not want you to make a special trip to the office only to learn that we are in court or otherwise unavailable.

Jail Visits

If your family member is currently in jail, we take that very seriously. We will visit your loved one and introduce ourselves. While the case is ongoing, we ask that a family member be designated a “contact” person so that messages can be relayed quickly. Never discuss the facts of the case over the phone with someone who is in jail. Jail calls are recorded and we have seen too many cases go south based on remarks made over recorded lines.

Police Reports and Discovery

We will do our best to provide you with copies of everything we receive on your case. Most information will be emailed, so please keep your email address up to date.

Changes in Contact Information

If you move or change numbers during the case, please let us know. It is difficult to help if we are unable to reach you, and helping you is why we are here.

Court Appearances

Cases do not get resolved as quickly as they do on television. Expect there to be several hearings in your case and it may be necessary for you to attend one or more of them. If a hearing is set, you will receive notice of the date and time of each hearing.

Billing and Collections

We understand that this investment was a huge decision for you. As we focus on providing the best representation, we will need for you to stay on schedule with any payment arrangements agreed to at the time of your initial consultation.

Again, thank you for your trust in us. We look forward to getting a fantastic outcome on your case.

Target Market(s)

Criminal defense clients and their families

Industry/Entity Type

Legal

Font styles to use
Serif

Requirements
Must have
• Must incorporate all of the rules we email out. Would like diagrams, images or pictures
Nice to have
• We attached a Welcome brochure. Not sure I want it to look super similar, hence the request for infographic.

```html
<!DOCTYPE html>
<html lang="en">
<head>
<meta charset="UTF-8">
<title>A Few Quick Rules – Client Onboarding</title>
<link rel="stylesheet" href="https://fonts.googleapis.com/css2?family=Oswald:wght@500;700&family=Open+Sans:wght@400;600&display=swap">
<style>
  :root{
    --navy:#1b2a45;
    --navy-deep:#14203a;
    --paper:#ffffff;
    --rule:#2b3446;
    --ink:#2a2f38;
    --sky:#dfe7f1;
  }
  *{margin:0;padding:0;box-sizing:border-box}
  html,body{width:820px;height:1200px;overflow:hidden;background:var(--rule)}
  .sheet{width:820px;height:1200px;position:relative;overflow:hidden;font-family:"Open Sans",Arial,sans-serif;color:var(--ink)}
  .masthead{height:170px;background:var(--navy);color:#fff;text-align:center;padding-top:16px}
  .masthead__kicker{font-family:"Oswald",Arial,sans-serif;font-weight:700;font-size:34px;letter-spacing:3px;line-height:1}
  .masthead__title{font-family:"Oswald",Arial,sans-serif;font-weight:700;font-size:58px;letter-spacing:3px;line-height:1.05;margin-top:2px}
  .masthead__intro{font-size:12.5px;line-height:1.45;width:600px;margin:8px auto 0;color:#e6e9ef}
  .grid{display:grid;grid-template-columns:repeat(3,1fr);grid-template-rows:420px 320px 281px;gap:3px;padding-top:3px}
  .rule-card{background:var(--paper);padding:14px 18px 12px;display:flex;flex-direction:column;text-align:center;overflow:hidden}
  .rule-card__title{font-family:"Oswald",Arial,sans-serif;font-weight:700;font-size:26px;line-height:1.05;color:var(--navy-deep);text-transform:uppercase;letter-spacing:.5px;margin-bottom:8px}
  .rule-card__text{font-size:12px;line-height:1.45;color:var(--ink)}
  .rule-card__art{margin:auto auto 0;width:190px;height:124px;border-radius:6px;flex-shrink:0}
  .rule-card--mid .rule-card__art{height:92px;width:170px}
  .art-calendar{background:linear-gradient(160deg,#f3f3f3,#c9ccd3)}
  .art-talk{background:linear-gradient(160deg,var(--sky),#9fb3cc)}
  .art-visit{background:linear-gradient(160deg,#f1e3d3,#b88d6a)}
  .art-court{background:linear-gradient(160deg,#eceef2,#7c8598)}
  .art-police{background:linear-gradient(160deg,#e6ebf2,#5f7394)}
  .art-phone{background:linear-gradient(160deg,#f2f4f7,#a5adba)}
  .signoff{grid-column:2 / span 2;background:var(--navy);color:#fff;display:flex;flex-direction:column;align-items:center;justify-content:center;text-align:center;padding:0 40px}
  .brand{display:flex;align-items:center;gap:12px}
  .brand__dot{width:14px;height:14px;border-radius:50%;background:#fff}
  .brand__name{font-family:"Oswald",Arial,sans-serif;font-weight:700;font-size:38px;letter-spacing:2px;text-transform:uppercase;color:#fff}
  .signoff__text{font-size:14px;line-height:1.5;margin-top:14px;max-width:400px;color:#e6e9ef}
</style>
</head>
<body>
<main class="sheet">
  <header class="masthead">
    <div class="masthead__kicker">A FEW</div>
    <h1 class="masthead__title">QUICK RULES</h1>
    <p class="masthead__intro">We are here to help each step of the way. While questions are never discouraged, this letter will answer some of the most common ones we get asked.</p>
  </header>

  <section class="grid">
    <article class="rule-card">
      <h2 class="rule-card__title">Appointments</h2>
      <p class="rule-card__text">One of the benefits of having an attorney is the ability to discuss your case outside of court, minus the stress and headaches. If you need an appointment, please contact the office. Appointments must be scheduled in advance. We do not want you to make a special trip to the office only to learn that we are in court or otherwise unavailable.</p>
      <div class="rule-card__art art-calendar" role="img" aria-label="Illustration of a desk calendar page"></div>
    </article>

    <article class="rule-card">
      <h2 class="rule-card__title">Communications</h2>
      <p class="rule-card__text">As a client, you should always be in the loop. While we will try to respond to questions as quickly as possible, sometimes we are unable to respond right away. Do not worry - we promise to get back to you soon. Some questions might take some time to research, and a correct answer is better than a quick one.</p>
      <div class="rule-card__art art-talk" role="img" aria-label="Illustration of two people talking with speech bubbles"></div>
    </article>

    <article class="rule-card">
      <h2 class="rule-card__title">Jail Visits</h2>
      <p class="rule-card__text">If your family member is currently in jail, we take that very seriously. We will visit your loved one and introduce ourselves. While the case is ongoing, we ask that a family member be designated a “contact” person so that messages can be relayed quickly. Never discuss the facts of the case over the phone with someone who is in jail. Jail calls are recorded and we have seen too many cases go south based on remarks made over recorded lines.</p>
      <div class="rule-card__art art-visit" role="img" aria-label="Illustration of a lawyer visiting a client at a jail table"></div>
    </article>

    <article class="rule-card rule-card--mid">
      <h2 class="rule-card__title">Court<br>Appearances</h2>
      <p class="rule-card__text">Cases do not get resolved as quickly as they do on television. Expect there to be several hearings in your case and it may be necessary for you to attend one or more of them. If a hearing is set, you will receive notice of the date and time of each hearing.</p>
      <div class="rule-card__art art-court" role="img" aria-label="Illustration of a judge at the bench with a gavel"></div>
    </article>

    <article class="rule-card rule-card--mid">
      <h2 class="rule-card__title">Police Reports<br>and Discovery</h2>
      <p class="rule-card__text">We will do our best to provide you with copies of everything we receive on your case. Most information will be emailed, so please keep your email address up to date.</p>
      <div class="rule-card__art art-police" role="img" aria-label="Illustration of police officers with case documents"></div>
    </article>

    <article class="rule-card rule-card--mid">
      <h2 class="rule-card__title">Changes in Contact<br>Information</h2>
      <p class="rule-card__text">If you move or change numbers during the case, please let us know. It is difficult to help if we are unable to reach you, and helping you is why we are here.</p>
      <div class="rule-card__art art-phone" role="img" aria-label="Illustration of a hand holding a mobile phone"></div>
    </article>

    <article class="rule-card">
      <h2 class="rule-card__title">Billing and<br>Collections</h2>
      <p class="rule-card__text">We understand that this investment was a huge decision for you. As we focus on providing the best representation, we will need for you to stay on schedule with any payment arrangements agreed to at the time of your initial consultation.</p>
    </article>

    <footer class="signoff">
      <div class="brand">
        <span class="brand__dot"></span>
        <span class="brand__name">Harbor Legal Group</span>
      </div>
      <p class="signoff__text">Again, thank you for your trust in us. We look forward to getting a fantastic outcome on your case.</p>
    </footer>
  </section>
</main>
</body>
</html>
```